Harlow Ridge Growers and Nursery needs a business street sign.

I have three businesses located at the same address: The Harlow Ridge Growers & Nursery, The Bramble Nook, and The Quarry Commons. I am looking for a 4’ x 8’ street sign to represent all three businesses as one retail experience. It needs to be eye catching yet simple enough that people can fully read it while driving by. I have logos for the greenhouse and village however I do not have anything for The Bramble Nook. I’m looking for some type of font that’s similar or in between the two attached logos for The Bramble Nook.

• Horizontal Sign, Eye catching, yet simple design so people see it while driving by.
• Horizontal Sign
• I’m open to the design being both vertical and horizontal. Please provide both options

```html
<!DOCTYPE html>
<html lang="en">
<head>
<meta charset="utf-8">
<title>Harlow Ridge Growers &amp; Nursery – Street Sign</title>
<link rel="stylesheet" href="https://fonts.googleapis.com/css2?family=Cabin:wght@600;700&display=swap">
<style>
  :root {
    --sign-green: #234a36;
    --sign-white: #ffffff;
    --wood-dark: #2a1517;
    --wood-mid: #34191c;
    --cream: #e9ead4;
    --band-plum: #7a3f45;
    --bloom-white: #f1f1ea;
    --bloom-leaf: #6fae94;
    --bloom-yellow: #efcf34;
  }
  html, body {
    margin: 0;
    width: 1200px;
    height: 587px;
    overflow: hidden;
    background: var(--sign-white);
  }
  .sign {
    position: relative;
    width: 1200px;
    height: 587px;
  }
  .sign-board {
    position: absolute;
    inset: 0;
  }
  .sign-text {
    position: absolute;
    margin: 0;
    font-family: "Cabin", "Trebuchet MS", sans-serif;
    font-weight: 700;
    color: var(--cream);
    line-height: 1;
    text-align: center;
    white-space: nowrap;
  }
  .greenhouse-name {
    left: 260px;
    width: 620px;
    top: 160px;
    font-size: 74px;
  }
  .greenhouse-tagline {
    left: 440px;
    width: 400px;
    top: 267px;
    font-size: 26px;
    letter-spacing: 0.5px;
    text-transform: uppercase;
  }
  .commons-name {
    left: 70px;
    width: 480px;
    top: 382px;
    font-size: 66px;
  }
  .nook-name {
    left: 625px;
    width: 540px;
    top: 382px;
    font-size: 66px;
  }
  .commons-name span,
  .nook-name span { display: block; }
  .commons-name span + span,
  .nook-name span + span { margin-top: 8px; }
</style>
</head>
<body>
<main class="sign">
  <svg class="sign-board" width="1200" height="587" viewBox="0 0 1200 587" aria-hidden="true">
    <defs>
      <clipPath id="sign-outline">
        <path id="sign-shape" d="M55,102 H385 C470,8 730,8 815,102 H1145 A55,55 0 0 0 1200,157 V530 A57,57 0 0 0 1143,587 H57 A57,57 0 0 0 0,530 V157 A55,55 0 0 0 55,102 Z"/>
      </clipPath>
      <linearGradient id="wood-tone" x1="0" y1="0" x2="1" y2="0">
        <stop offset="0" stop-color="var(--wood-dark)"/>
        <stop offset="0.5" stop-color="var(--wood-mid)"/>
        <stop offset="1" stop-color="var(--wood-dark)"/>
      </linearGradient>
    </defs>
    <g clip-path="url(#sign-outline)">
      <use href="#sign-shape" fill="url(#wood-tone)"/>
      <use href="#sign-shape" fill="none" stroke="var(--sign-white)" stroke-width="56"/>
      <use href="#sign-shape" fill="none" stroke="var(--sign-green)" stroke-width="26"/>
    </g>
    <rect class="tagline-band" x="428" y="259" width="421" height="44" rx="9" fill="var(--band-plum)" stroke="var(--sign-green)" stroke-width="2"/>
  </svg>

  <svg class="sign-board" width="1200" height="587" viewBox="0 0 1200 587">
    <defs>
      <linearGradient id="bloom-tone" x1="0" y1="0" x2="1" y2="0">
        <stop offset="0" stop-color="var(--bloom-leaf)"/>
        <stop offset="0.35" stop-color="var(--bloom-white)"/>
        <stop offset="0.55" stop-color="var(--bloom-yellow)"/>
        <stop offset="0.7" stop-color="var(--bloom-white)"/>
        <stop offset="1" stop-color="var(--bloom-leaf)"/>
      </linearGradient>
    </defs>
    <rect class="flower-spray" role="img" aria-label="Spray of white and yellow daisies with green leaves" x="532" y="52" width="176" height="64" rx="30" fill="url(#bloom-tone)"/>
  </svg>

  <h1 class="sign-text greenhouse-name">The Harlow Ridge</h1>
  <p class="sign-text greenhouse-tagline">Growers &amp; Nursery</p>

  <p class="sign-text commons-name"><span>Quarry</span><span>Commons</span></p>

  <p class="sign-text nook-name"><span>The Bramble</span><span>Nook</span></p>
</main>
</body>
</html>
```